New business card for UK roofing company

We are Brindmore Roofing and we need a business card design for our staff.

We offer the following services:

- New roofs
- General roof repairs
- Drone surveys
- Single ply roofing
- Steel cladding
- Asbestos removal
- Electronic leak detection

I have attached our logo. I have also attached example branding printed to our vans. The business card should fit in with the style of our branding.

The business card should have the following information;

Address:
Unit 17c Wendlecroft Farm
Wendlecroft Lane
Hatchington
CM4 9QD

Telephone: 020 7946 0372
24 Hour: 0800 612 4479

Email: ray@brindmoreroofing.example
Mobile: 07700981234
Name: Ray Tunstead
Website: www.brindmoreroofing.example

The business card will be printed in Spot UV, see here: https://www.kestaprint.example/business-cards/spot-uv/

If you need anymore info, please let me know,

```html
<!DOCTYPE html>
<html lang="en">
<head>
<meta charset="utf-8">
<title>Brindmore Roofing – Business Card</title>
<link rel="stylesheet" href="https://fonts.googleapis.com/css2?family=Arimo:wght@400;700&family=Roboto+Condensed:wght@700&display=swap">
<style>
  :root {
    --navy: #0f4a7c;
    --cyan: #00aedb;
    --white: #ffffff;
    --backdrop: #adadad;
  }
  * { margin: 0; padding: 0; box-sizing: border-box; }
  html, body { width: 1200px; height: 1000px; overflow: hidden; }
  body {
    background: var(--backdrop);
    font-family: "Arimo", Arial, sans-serif;
    position: relative;
  }
  .card {
    position: absolute;
    left: 294px;
    width: 613px;
    height: 352px;
    border-radius: 24px;
    overflow: hidden;
    background: var(--white);
  }
  .card--front { top: 80px; }
  .card--back { top: 496px; }

  /* Front */
  .front-panel {
    position: absolute; left: 0; top: 0; width: 100%; height: 255px;
    background: var(--navy);
  }
  .front-stripe {
    position: absolute; left: 0; top: 255px; width: 100%; height: 18px;
    background: var(--cyan);
  }
  .front-rule {
    position: absolute; left: 0; top: 273px; width: 100%; height: 9px;
    background: var(--navy);
  }
  .brand {
    position: absolute; display: flex; align-items: center;
    color: var(--white); font-weight: 700; letter-spacing: -1px;
  }
  .brand__dot {
    border-radius: 50%; background: var(--cyan); flex: none;
  }
  .front-brand { left: 60px; top: 38px; font-size: 50px; gap: 12px; }
  .front-brand .brand__dot { width: 52px; height: 52px; }
  .tagline { position: absolute; color: var(--white); font-weight: 700; }
  .front-tagline { left: 0; width: 100%; text-align: center; top: 106px; font-size: 22px; letter-spacing: 0.3px; }
  .phone-main {
    position: absolute; left: 148px; top: 153px;
    display: flex; align-items: center; gap: 6px;
    font-family: "Roboto Condensed", "Arial Narrow", sans-serif;
    font-size: 46px; color: var(--cyan); line-height: 1;
  }
  .phone-main svg { width: 30px; height: 30px; }
  .phone-24 {
    position: absolute; left: 149px; top: 202px;
    font-size: 28px; color: var(--white); line-height: 1;
  }
  .phone-24 strong { font-weight: 700; }
  .services {
    position: absolute; left: 0; top: 294px; width: 100%;
    text-align: center; color: var(--navy); font-weight: 700;
    font-size: 16.5px; line-height: 21px; letter-spacing: 0.2px;
  }

  /* Back */
  .back-header { position: absolute; left: 0; top: 0; }
  .back-accent { position: absolute; left: 250px; top: 20px; }
  .back-brand { left: 34px; top: 32px; font-size: 27px; gap: 6px; }
  .back-brand .brand__dot { width: 26px; height: 26px; }
  .back-tagline { left: 78px; top: 64px; font-size: 12.5px; }
  .contact {
    position: absolute; left: 39px; top: 153px;
    color: var(--navy); font-size: 14px; line-height: 17px;
  }
  .contact__name { font-size: 18.5px; font-weight: 700; letter-spacing: 0.3px; margin-bottom: 12px; }
  .contact__group { margin-bottom: 16px; }
  .contact__web { font-weight: 700; }
</style>
</head>
<body>

<section class="card card--front" aria-label="Business card front">
  <div class="front-panel"></div>
  <div class="front-stripe"></div>
  <div class="front-rule"></div>

  <div class="brand front-brand">
    <span class="brand__dot"></span>
    <span class="brand__name">brindmoreroofing</span>
  </div>
  <p class="tagline front-tagline">Your local roofing experts</p>

  <p class="phone-main">
    <svg viewBox="0 0 24 24" aria-hidden="true"><path fill="#00aedb" d="M6.6 10.8a15.1 15.1 0 0 0 6.6 6.6l2.2-2.2c.3-.3.7-.4 1-.2 1.1.4 2.3.6 3.6.6.6 0 1 .4 1 1V20c0 .6-.4 1-1 1A17 17 0 0 1 3 4c0-.6.4-1 1-1h3.5c.6 0 1 .4 1 1 0 1.3.2 2.5.6 3.6.1.3 0 .7-.2 1z"/></svg>
    020 7946 0372
  </p>
  <p class="phone-24"><strong>24 Hour:</strong> 0800 612 4479</p>

  <p class="services">
    New roofs | General roof repairs | Drone surveys| Single ply roofing<br>
    Steel cladding | Asbestos removal | Electronic leak detection
  </p>
</section>

<section class="card card--back" aria-label="Business card back">
  <svg class="back-header" width="613" height="352" viewBox="0 0 613 352" aria-hidden="true">
    <polygon points="0,0 613,0 613,74 0,112" fill="#0f4a7c"/>
    <polygon points="0,112 613,74 613,88 0,126" fill="#00aedb"/>
    <polygon points="0,126 613,88 613,95 0,134" fill="#0f4a7c"/>
    <circle cx="470" cy="225" r="178" fill="#ffffff"/>
    <circle cx="470" cy="225" r="168" fill="#00aedb"/>
  </svg>

  <div class="brand back-brand">
    <span class="brand__dot"></span>
    <span class="brand__name">brindmoreroofing</span>
  </div>
  <p class="tagline back-tagline">Your local roofing experts</p>

  <div class="contact">
    <p class="contact__name">Ray Tunstead</p>
    <p class="contact__group">ray@brindmoreroofing.example<br>07700981234</p>
    <p class="contact__group">Unit 17c Wendlecroft Farm,<br>Wendlecroft Lane, Hatchington,<br>Marlowbridge CM4 9QD</p>
    <p class="contact__web">www.brindmoreroofing.example</p>
  </div>
</section>

</body>
</html>
```